Label Redesign For Hemp Oil Tincture Bottle*

I need a label redesigned for Marbleleaf Hemp, current bottle label and logo is attached. The current label doesn't standout, not sure if its the font size or colors on the existing label. It is very important to have on the label that this is a Premium Full Spectrum Hemp Oil that is 2000mg. Then after the label is redesigned and approved, I would need to packaging to be designed to match the approved label design.
This Hemp oil has a relaxing effect to help ease mental and emotional stress, tension and worry. The Omega Fatty Acids it contains also naturally improves your mood and overall brain function, causing you to feel more alert and focused. Hemp Oil helps with insomnia. Take some 2-3 hours before bedtime, you will feel relaxed yet aware of how tired you are that it will lead to a good night's sleep. Hemp Oil helps ease chronic pain and inflammation from conditions such as arthritis, fibromyalgia, lupus, and MS. As a pain relief supplement, it is a safer, natural, non-chemical and non-addictive alternative to prescription painkillers.

Target Market(s)

Adults

Industry/Entity Type

Supplement

Font styles to use
Serif
Sans Serif

Colors

Designer to choose colors to be used in the design.

Requirements
Must have
• All information thats on current label but where it says 750 in the front of the existing label, it needs to say 2000. The 2000 should be prominent on the label.

```html
<!DOCTYPE html>
<html lang="en">
<head>
<meta charset="utf-8">
<title>Marbleleaf Hemp – Tincture Label</title>
<link rel="stylesheet" href="https://fonts.googleapis.com/css2?family=Cormorant+Garamond:wght@600;700&family=Lato:wght@700&display=swap">
<style>
  :root {
    --page-bg: #e4e4e4;
    --cream: #e7ecd3;
    --cream-pale: #eef2de;
    --green-deep: #2f7f55;
    --green-mid: #47a04d;
    --green-light: #a3d28f;
    --green-band: #4cae4c;
    --ink: #1d2a1b;
    --label-text: #eef0d6;
  }
  html, body {
    margin: 0;
    padding: 0;
    width: 969px;
    height: 1200px;
    overflow: hidden;
    background: var(--page-bg);
  }
  .label {
    position: absolute;
    left: 44px;
    top: 15px;
    width: 880px;
    height: 1169px;
    display: block;
  }
  .serif { font-family: "Cormorant Garamond", Georgia, serif; font-weight: 700; }
  .sans { font-family: "Lato", Arial, sans-serif; font-weight: 700; }
  .on-green { fill: var(--label-text); }
  .on-cream { fill: var(--ink); }
</style>
</head>
<body>
<svg class="label" viewBox="447 690 350 465" xmlns="http://www.w3.org/2000/svg" aria-label="Marbleleaf Hemp Premium Full Spectrum 2000mg hemp oil label">
  <defs>
    <linearGradient id="top-field" x1="0" y1="0" x2="1" y2="0">
      <stop offset="0" stop-color="#3f9a4f"/>
      <stop offset="0.55" stop-color="#5fb25c"/>
      <stop offset="1" stop-color="var(--green-light)"/>
    </linearGradient>
    <linearGradient id="seal-fill" x1="0" y1="0" x2="1" y2="1">
      <stop offset="0" stop-color="#4fa24f"/>
      <stop offset="1" stop-color="var(--green-deep)"/>
    </linearGradient>
    <linearGradient id="bottom-band" x1="0" y1="0" x2="0" y2="1">
      <stop offset="0" stop-color="#5cb85a"/>
      <stop offset="1" stop-color="#3f9d45"/>
    </linearGradient>
  </defs>

  <!-- base -->
  <rect class="label-base" x="447" y="690" width="350" height="465" fill="var(--cream)"/>

  <!-- upper green field -->
  <path class="top-field" d="M447,690 H797 V905 Q700,965 447,1002 Z" fill="url(#top-field)"/>
  <rect class="edge-panel" x="771" y="690" width="26" height="330" fill="var(--cream-pale)" opacity="0.75"/>

  <!-- central seal -->
  <circle class="seal" cx="617" cy="826" r="150" fill="url(#seal-fill)"/>

  <!-- brand mark area -->
  <circle class="brand-dot" cx="617" cy="723" r="15" fill="var(--label-text)"/>
  <text class="sans on-green" x="622" y="770" font-size="12" text-anchor="middle">Zero THC</text>

  <!-- product name block -->
  <text class="serif on-green" x="624" y="813" font-size="22" text-anchor="middle">Marbleleaf Hemp</text>
  <text class="serif on-green" x="620" y="855" font-size="21" text-anchor="middle" letter-spacing="0.5">PREMIUM</text>
  <text class="serif on-green" x="625" y="885" font-size="21" text-anchor="middle" letter-spacing="0.5">FULL SPECTRUM</text>
  <text class="serif on-green" x="623" y="918" font-size="22" text-anchor="middle">2000mg</text>
  <text class="sans on-green" x="624" y="960" font-size="18" text-anchor="middle">HEMP OIL</text>

  <!-- supplement info -->
  <text class="serif on-cream" x="624" y="1010" font-size="17" text-anchor="middle">2000mg</text>
  <text class="serif on-cream" x="609" y="1034" font-size="17" text-anchor="middle">Dietary Supplement</text>

  <!-- bottom band -->
  <path class="bottom-band" d="M447,1096 Q622,1068 797,1096 V1155 H447 Z" fill="url(#bottom-band)"/>
  <text class="serif on-cream" x="622" y="1102" font-size="14" text-anchor="middle">1 FL. OZ (30 ML)</text>
  <text class="serif on-cream" x="623" y="1129" font-size="16" text-anchor="middle">Natural Peppermint Flavor</text>
</svg>
</body>
</html>
```